Redesign of Business Cards to Update them!

We want a full overhaul of our business cards! We have a design that is almost 5 years old and it needs to be updated to be current

Address is 437 Dunmore Lane Suite 4 Brookvale NV 89412
PH: 9094718263
Zorlivo.com

Hours M-F 10AM-4PM
Sat and Sunday Closed

```html
<!DOCTYPE html>
<html lang="en">
<head>
<meta charset="utf-8">
<title>Zorlivo Business Card</title>
<link rel="stylesheet" href="https://fonts.googleapis.com/css2?family=Questrial&display=swap">
<style>
  :root {
    --bg: #c9c9c9;
    --paper: #f4f4f4;
    --ink: #252525;
    --red: #ef0000;
    --white: #ffffff;
    --rule: #8a8a8a;
  }
  * { box-sizing: border-box; margin: 0; padding: 0; }
  html, body {
    width: 1200px; height: 800px; overflow: hidden;
    background: var(--bg);
    font-family: "Questrial", "Century Gothic", sans-serif;
  }
  .canvas {
    width: 1200px; height: 800px;
    display: flex; align-items: center; justify-content: center; gap: 50px;
  }
  .card {
    width: 540px; height: 309px;
    border-radius: 22px; overflow: hidden; position: relative;
    box-shadow: 0 10px 24px rgba(0,0,0,0.25);
  }
  /* Front */
  .card-front { background: var(--paper); }
  .brand-area {
    height: 168px; display: flex; align-items: center; justify-content: center; gap: 14px;
  }
  .brand-dot { width: 26px; height: 26px; border-radius: 50%; background: var(--red); }
  .brand-name { font-size: 46px; color: var(--ink); letter-spacing: 1px; }
  .accent-line { height: 3px; background: var(--red); }
  .info-band {
    position: absolute; left: 0; right: 0; top: 171px; bottom: 0;
    background: var(--ink);
    display: flex; align-items: center; padding: 0 34px;
  }
  .person { width: 190px; color: var(--white); }
  .person-name { font-size: 20px; letter-spacing: 1px; text-transform: uppercase; }
  .person-title { font-size: 14px; color: var(--red); margin-top: 2px; }
  .divider { width: 1px; height: 64px; background: var(--rule); margin-right: 26px; }
  .contacts { list-style: none; color: var(--white); font-size: 13px; line-height: 1.45; }
  .contacts li { display: flex; align-items: flex-start; gap: 8px; }
  .contacts svg { width: 11px; height: 11px; margin-top: 3px; flex: none; fill: var(--red); }
  .contacts .no-icon { padding-left: 19px; }
  /* Back */
  .card-back {
    background: var(--red);
    display: flex; flex-direction: column; align-items: center; justify-content: center;
  }
  .back-brand { font-size: 54px; color: var(--white); letter-spacing: 1px; }
  .hours {
    position: absolute; bottom: 34px; left: 0; right: 0;
    text-align: center; color: var(--white); font-size: 14px; word-spacing: 1px;
  }
  .hours span { margin-left: 14px; }
</style>
</head>
<body>
<main class="canvas">
  <section class="card card-front">
    <div class="brand-area">
      <span class="brand-dot"></span>
      <span class="brand-name">Zorlivo</span>
    </div>
    <div class="accent-line"></div>
    <div class="info-band">
      <div class="person">
        <div class="person-name">Daniel Reyes</div>
        <div class="person-title">President</div>
      </div>
      <div class="divider"></div>
      <ul class="contacts">
        <li>
          <svg viewBox="0 0 10 10"><path d="M5 0a3.5 3.5 0 0 0-3.5 3.5C1.5 6 5 10 5 10s3.5-4 3.5-6.5A3.5 3.5 0 0 0 5 0zm0 5a1.4 1.4 0 1 1 0-2.8A1.4 1.4 0 0 1 5 5z"/></svg>
          437 Dunmore Lane, Suite 4
        </li>
        <li class="no-icon">Brookvale NV 89412</li>
        <li>
          <svg viewBox="0 0 10 10"><path d="M2.2 0.5 3.8 2.6 2.9 3.6c.6 1.4 2 2.8 3.5 3.5l1-0.9 2.1 1.6-1 1.5C4.5 9.2.8 5.5.7 1.6z"/></svg>
          909-471-8263
        </li>
        <li>
          <svg viewBox="0 0 10 10"><path d="M5 0a5 5 0 1 0 0 10A5 5 0 0 0 5 0zm0 1.2c.6.7 1 1.7 1.1 3.2H3.9C4 2.9 4.4 1.9 5 1.2zM1.3 5.6h1.5c.1 1.2.4 2.2.9 2.9A3.9 3.9 0 0 1 1.3 5.6zm0-1.2A3.9 3.9 0 0 1 3.7 1.5c-.5.7-.8 1.7-.9 2.9zm3.7 4.4c-.6-.7-1-1.7-1.1-3.2h2.2C6 7.1 5.6 8.1 5 8.8zm1.3-.3c.5-.7.8-1.7.9-2.9h1.5a3.9 3.9 0 0 1-2.4 2.9zm.9-4.1c-.1-1.2-.4-2.2-.9-2.9a3.9 3.9 0 0 1 2.4 2.9z"/></svg>
          Zorlivo.com
        </li>
      </ul>
    </div>
  </section>

  <section class="card card-back">
    <div class="back-brand">Zorlivo</div>
    <p class="hours">Hours : M-F 10 AM- 4 PM <span>Sat &amp; Sunday Closed</span></p>
  </section>
</main>
</body>
</html>
```